first fantastic look and impression

We are looking for a concept for letterhead, business card, emailfooter and template for invoices or offers for our company in the consultation business.
The dancer is a symbol who we are: it looks simple, but there is a lot of hard work and many years of training in this movement. The look is also what we want: elegant, modern, strong, with a touch of extravaganza
Target Market(s)
Hotelbusiness , Consulting
Font styles to use
Sans Serif
Other font styles liked:
- please give us a option we are open
Requirements
Must have
- We are not typical consultants but sparring partners and coaches for the hotel and that should also be expressed in the design. Maybe there is an icon that supports the whole thing. We are more modern and bolder than our industry colleagues.
we are modern, fresh, agile, fast
Nice to have
- a icon

```html
<!DOCTYPE html>
<html lang="en">
<head>
<meta charset="utf-8">
<title>Business Card – Front and Back</title>
<link rel="stylesheet" href="https://fonts.googleapis.com/css2?family=Khand:wght@500&family=Roboto:wght@400&display=swap">
<style>
  :root {
    --backdrop: #6e6e6e;
    --card: #161616;
    --emboss-dark: #1c1c1c;
    --emboss-light: #2c2c2c;
    --silver-light: #e6e6e6;
    --silver-dark: #8a8a8a;
    --text-main: #e2e2e2;
    --text-soft: #c6c6c6;
  }
  * { box-sizing: border-box; margin: 0; padding: 0; }
  html, body {
    width: 1200px;
    height: 1138px;
    overflow: hidden;
    background: var(--backdrop);
  }
  .canvas {
    position: relative;
    width: 1200px;
    height: 1138px;
  }
  .card {
    position: absolute;
    width: 620px;
    height: 374px;
    background: var(--card);
    border-radius: 16px;
  }
  .card--front { left: 274px; top: 186px; }
  .card--back  { left: 276px; top: 608px; width: 618px; }

  .artwork {
    position: absolute;
    border-radius: 40% 45% 42% 48%;
  }
  .artwork--emboss {
    left: 162px; top: 62px; width: 300px; height: 276px;
    background: radial-gradient(ellipse at 45% 45%, var(--emboss-light), var(--emboss-dark) 70%, var(--card));
  }
  .artwork--foil {
    left: 32px; top: 52px; width: 284px; height: 268px;
    background: radial-gradient(ellipse at 40% 40%, var(--silver-dark), #3a3a3a 65%, var(--card));
  }

  .brand {
    position: absolute;
    right: 34px;
    top: 52px;
    font-family: "Roboto", sans-serif;
    font-weight: 400;
    font-size: 36px;
    line-height: 1;
    color: var(--silver-light);
    letter-spacing: 0.5px;
  }
  .person {
    position: absolute;
    right: 34px;
    top: 157px;
    text-align: right;
  }
  .person__name {
    font-family: "Khand", sans-serif;
    font-weight: 500;
    font-size: 27px;
    line-height: 1;
    color: var(--text-main);
  }
  .person__role {
    margin-top: 7px;
    font-family: "Roboto", sans-serif;
    font-size: 14.5px;
    color: var(--text-soft);
  }
  .contacts {
    position: absolute;
    right: 34px;
    top: 240px;
    list-style: none;
    font-family: "Roboto", sans-serif;
    font-size: 14.5px;
    color: var(--text-soft);
    text-align: right;
  }
  .contacts__item {
    display: flex;
    justify-content: flex-end;
    align-items: center;
    gap: 10px;
    height: 24px;
  }
  .contacts__icon { width: 14px; height: 14px; fill: var(--text-soft); }
  .contacts__address { margin-top: 6px; height: 24px; line-height: 24px; }
</style>
</head>
<body>
<main class="canvas">
  <section class="card card--front" aria-label="Card front">
    <div class="artwork artwork--emboss" role="img" aria-label="Embossed line illustration of a leaping dancer holding flowing fabric"></div>
  </section>

  <section class="card card--back" aria-label="Card back">
    <div class="artwork artwork--foil" role="img" aria-label="Silver foil line illustration of a leaping dancer holding flowing fabric"></div>

    <div class="brand">Kessler Roth</div>

    <div class="person">
      <div class="person__name">John Doe Smith</div>
      <div class="person__role">Managing Director</div>
    </div>

    <ul class="contacts">
      <li class="contacts__item">828-111-1111
        <svg class="contacts__icon" viewBox="0 0 16 16" aria-hidden="true"><path d="M3 5c0-2 2-3 5-3s5 1 5 3v1h-3V5H6v1H3zM4 8l2-2h4l2 2v5H4zm4 1.2a1.6 1.6 0 1 0 0 3.2 1.6 1.6 0 0 0 0-3.2z"/></svg>
      </li>
      <li class="contacts__item">john@yourwebsite.com
        <svg class="contacts__icon" viewBox="0 0 16 16" aria-hidden="true"><path d="M1 3h14v10H1zm1.5 1.3L8 8.5l5.5-4.2zM2 12h12V5.4L8 10 2 5.4z"/></svg>
      </li>
      <li class="contacts__item">www.yourwebsite.com
        <svg class="contacts__icon" viewBox="0 0 16 16" aria-hidden="true"><path d="M8 1a7 7 0 1 0 0 14A7 7 0 0 0 8 1zm-1 1.6V5H4.2A5.6 5.6 0 0 1 7 2.6zm2 0A5.6 5.6 0 0 1 11.8 5H9zM3.6 6H7v1.5H3.1c.1-.5.2-1 .5-1.5zm5.4 0h3.4c.3.5.4 1 .5 1.5H9zM3.1 8.5H7V10H3.6a5 5 0 0 1-.5-1.5zm5.9 0h3.9a5 5 0 0 1-.5 1.5H9zM4.2 11H7v2.4A5.6 5.6 0 0 1 4.2 11zM9 11h2.8A5.6 5.6 0 0 1 9 13.4z"/></svg>
      </li>
      <li class="contacts__address">234 Anywhere St., Any City, US 123456</li>
    </ul>
  </section>
</main>
</body>
</html>
```